Morrow Real Etate
Morrow Real Estate
Use same font as used in my logo
Use what ever look best
Neil Morrow
Broker/Owner
518 Pellam St.
Harlow KS 47096
nmorrow@MorrowREq.com
MorrowREq.com
Need design for Business Cards, Letterhead and Envelopes.
Logo AI file.

```html
<!DOCTYPE html>
<html lang="en">
<head>
<meta charset="utf-8">
<title>Morrow Real Estate – Business Card</title>
<link rel="stylesheet" href="https://fonts.googleapis.com/css2?family=Arimo:wght@400;700&family=Tinos:wght@400&display=swap">
<style>
  :root {
    --backdrop: #3a3a3a;
    --card: #ffffff;
    --brand-blue: #1f63b5;
    --band-dark: #151515;
    --ink: #1a1a1a;
    --rule: #b9b9b9;
    --icon: #3d4a5c;
  }
  * { margin: 0; padding: 0; box-sizing: border-box; }
  html, body {
    width: 1200px; height: 780px; overflow: hidden;
    background: var(--backdrop);
  }
  .business-card {
    position: absolute;
    left: 80px; top: 93px;
    width: 1040px; height: 594px;
    background: var(--card);
    border-radius: 34px;
    overflow: hidden;
  }
  .card-bands {
    position: absolute; left: 0; top: 0;
    width: 1040px; height: 594px;
  }
  .brand {
    position: absolute;
    left: 150px; top: 92px;
    display: flex; align-items: center; gap: 20px;
    font-family: "Arimo", sans-serif;
    font-weight: 700;
    font-size: 62px;
    line-height: 1;
    color: var(--brand-blue);
    letter-spacing: -1px;
    white-space: nowrap;
  }
  .brand-mark {
    width: 52px; height: 52px;
    background: var(--brand-blue);
  }
  .divider {
    position: absolute;
    left: 522px; top: 250px;
    width: 2px; height: 200px;
    background: var(--rule);
  }
  .agent {
    position: absolute;
    right: 548px; top: 290px;
    text-align: right;
    white-space: nowrap;
  }
  .agent-name {
    font-family: "Arimo", sans-serif;
    font-weight: 700;
    font-size: 31px;
    line-height: 1.1;
    color: var(--brand-blue);
  }
  .agent-title {
    font-family: "Arimo", sans-serif;
    font-weight: 700;
    font-size: 19px;
    color: var(--ink);
    margin-top: 4px;
  }
  .agent-address {
    font-family: "Tinos", serif;
    font-size: 24px;
    line-height: 1.2;
    color: var(--ink);
    margin-top: 24px;
  }
  .contact-list {
    position: absolute;
    left: 548px; top: 256px;
    list-style: none;
    font-family: "Tinos", serif;
    font-size: 24px;
    color: var(--ink);
    white-space: nowrap;
  }
  .contact-list li {
    display: flex; align-items: center; gap: 12px;
    height: 38px;
  }
  .contact-list svg { width: 22px; height: 22px; flex: none; }
</style>
</head>
<body>
  <div class="business-card">
    <svg class="card-bands" viewBox="0 0 1040 594" aria-hidden="true">
      <polygon points="0,522 600,522 582,556 0,556" fill="var(--brand-blue)"/>
      <polygon points="615,522 1040,478 1040,594 592,594 592,560" fill="var(--band-dark)"/>
    </svg>

    <div class="brand">
      <span class="brand-name">Morrow Real Estate</span>
      <span class="brand-mark"></span>
    </div>

    <div class="divider"></div>

    <div class="agent">
      <div class="agent-name">Neil Morrow</div>
      <div class="agent-title">Broker/Owner</div>
      <div class="agent-address">518 Pellam St.<br>Harlow KS 47096</div>
    </div>

    <ul class="contact-list">
      <li>
        <svg viewBox="0 0 24 24"><path d="M6 2h4l2 5-3 2a12 12 0 0 0 6 6l2-3 5 2v4c0 2-2 4-4 4C9 22 2 15 2 6c0-2 2-4 4-4z" fill="var(--icon)"/></svg>
        <span>555 210 4800</span>
      </li>
      <li>
        <svg viewBox="0 0 24 24"><rect x="7" y="2" width="10" height="20" rx="2" fill="var(--icon)"/><rect x="9" y="5" width="6" height="9" fill="#fff"/></svg>
        <span>555 318 4800</span>
      </li>
      <li>
        <svg viewBox="0 0 24 24"><rect x="7" y="2" width="10" height="7" fill="var(--icon)"/><rect x="3" y="9" width="18" height="9" rx="2" fill="var(--icon)"/><rect x="7" y="15" width="10" height="7" fill="var(--icon)" stroke="#fff" stroke-width="1.5"/></svg>
        <span>555 210 4825</span>
      </li>
      <li>
        <svg viewBox="0 0 24 24"><text x="12" y="19" text-anchor="middle" font-family="Arimo, sans-serif" font-weight="700" font-size="22" fill="var(--icon)">@</text></svg>
        <span>nmorrow@MorrowREq.com</span>
      </li>
      <li>
        <svg viewBox="0 0 24 24"><circle cx="12" cy="12" r="10" fill="var(--icon)"/><path d="M2 12h20M12 2c4 4 4 16 0 20M12 2c-4 4-4 16 0 20" stroke="#fff" stroke-width="1.4" fill="none"/></svg>
        <span>www.MorrowREq.com</span>
      </li>
    </ul>
  </div>
</body>
</html>
```